Coffeeshop menu for filter tip

We want to have a cannabis (coffeeshop) menu in the size 25mm wide x 60mm wide. Some examples attached.

it must have the following text:
Menu

WEED p/g
Velotrine €16
Cinderfox €14
Tide Rambler €14
Marigolden €16
Grand Pelican €14
Copper Comet €14

HASH p/g
Baltic Ember €12
Harbor Velvet€11
Plum Rova €14
Dusk Maple €10

Target Market(s)

tourist in Amsterdam

Requirements
Nice to have
• cannabis sign leaf
• No Cigarettes allowed symbol

```html
<!DOCTYPE html>
<html lang="en">
<head>
<meta charset="utf-8">
<title>Menu – Coffeeshop Amsterdam</title>
<link rel="stylesheet" href="https://fonts.googleapis.com/css2?family=EB+Garamond:wght@400&family=Open+Sans:wght@400&display=swap">
<style>
  :root {
    --ink: #111111;
    --paper-top: #e9e8ec;
    --paper-mid: #e2d9d0;
    --burn-tan: #c99c73;
    --burn-deep: #8a5a38;
    --lavender: #dedae7;
    --lavender-soft: #e8e4ee;
    --panel: rgba(250, 249, 252, 0.72);
    --leaf: #ffffff;
  }
  * { margin: 0; padding: 0; box-sizing: border-box; }
  html, body { width: 1200px; height: 500px; overflow: hidden; background: #ffffff; }
  .menu-card {
    position: relative;
    width: 1200px;
    height: 500px;
    overflow: hidden;
    background: var(--lavender);
    font-family: "Open Sans", sans-serif;
    color: var(--ink);
  }
  .backdrop-right {
    position: absolute;
    left: 528px; top: 0;
    width: 672px; height: 500px;
    background: linear-gradient(180deg, var(--lavender-soft) 0%, var(--lavender) 55%, #e2dde6 100%);
  }
  .burnt-paper {
    position: absolute;
    left: 0; top: 0;
    width: 532px; height: 500px;
    background: linear-gradient(172deg, var(--paper-top) 0%, var(--paper-top) 34%, var(--paper-mid) 50%, var(--burn-tan) 72%, #b88863 100%);
  }
  .leaf-mark {
    position: absolute;
    left: 372px; top: 348px;
    width: 190px; height: 152px;
    background: radial-gradient(ellipse at 50% 60%, rgba(255,255,255,0.85) 0%, rgba(255,255,255,0.45) 45%, rgba(255,255,255,0) 72%);
  }
  .title-block {
    position: absolute;
    left: 44px; top: 58px;
  }
  .title {
    display: block;
    width: 341px;
    padding-left: 176px;
    font-family: "EB Garamond", serif;
    font-size: 60px;
    line-height: 62px;
    font-weight: 400;
    border-bottom: 3px solid var(--ink);
  }
  .subtitle {
    display: block;
    margin: 6px 0 0 7px;
    font-family: "EB Garamond", serif;
    font-size: 32px;
    line-height: 36px;
  }
  .price-panel {
    position: absolute;
    top: 73px;
    width: 261px;
    height: 350px;
    background: var(--panel);
  }
  .price-panel--weed { left: 579px; }
  .price-panel--hash { left: 890px; }
  .panel-heading {
    position: absolute;
    left: 10px; top: 14px;
    display: flex;
    align-items: flex-end;
    font-family: "EB Garamond", serif;
    font-weight: 400;
  }
  .panel-heading .label {
    display: block;
    width: 180px;
    font-size: 36px;
    line-height: 36px;
    border-bottom: 1.5px solid var(--ink);
  }
  .panel-heading .unit {
    font-size: 11px;
    line-height: 14px;
    margin-left: 3px;
    margin-bottom: 2px;
  }
  .price-list {
    position: absolute;
    left: 10px;
    width: 190px;
    list-style: none;
  }
  .price-list li {
    display: flex;
    justify-content: space-between;
    font-size: 17px;
    line-height: 24px;
  }
  .price-panel--weed .price-list { top: 94px; }
  .price-panel--weed .price-list li { margin-bottom: 17px; }
  .price-panel--hash .price-list { top: 117px; left: 24px; width: 200px; }
  .price-panel--hash .price-list li { margin-bottom: 27.5px; }
</style>
</head>
<body>
<main class="menu-card">
  <div class="backdrop-right" role="img" aria-label="Soft lavender paper texture background"></div>
  <div class="burnt-paper" role="img" aria-label="Photo of torn paper with burnt, charred edges"></div>
  <div class="leaf-mark" role="img" aria-label="White cannabis leaf symbol"></div>

  <header class="title-block">
    <h1 class="title">Menu</h1>
    <p class="subtitle">Coffeeshop Amsterdam</p>
  </header>

  <section class="price-panel price-panel--weed">
    <h2 class="panel-heading"><span class="label">WEED</span><span class="unit">(p/g)</span></h2>
    <ul class="price-list">
      <li><span>Velotrine</span><span>€16</span></li>
      <li><span>Cinderfox</span><span>€14</span></li>
      <li><span>Tide Rambler</span><span>€14</span></li>
      <li><span>Marigolden</span><span>€16</span></li>
      <li><span>Grand Pelican</span><span>€14</span></li>
      <li><span>Copper Comet</span><span>€14</span></li>
    </ul>
  </section>

  <section class="price-panel price-panel--hash">
    <h2 class="panel-heading"><span class="label">HASH</span><span class="unit">(p/g)</span></h2>
    <ul class="price-list">
      <li><span>Baltic Ember</span><span>€12</span></li>
      <li><span>Harbor Velvet</span><span>€11</span></li>
      <li><span>Plum Rova</span><span>€14</span></li>
      <li><span>Dusk Maple</span><span>€10</span></li>
    </ul>
  </section>
</main>
</body>
</html>
```